Stationery Design Project

We are looking for a full revision of our existing stationary to include within this project:

- Letterhead
- Business card
- Compliment slip

The items should be a reflection of our new website which can be found at http://www.larkfieldchecks.co.uk/

Our logo files are included within the file brief

There are some further projects which we may approach the winning designer for as we need a revision to the front cover of our reports, a new price list and two brochures for specific target markets.

Industry/Entity Type

Business

```html
<!DOCTYPE html>
<html lang="en">
<head>
<meta charset="utf-8">
<title>Larkfield Checks – Business Card</title>
<link rel="stylesheet" href="https://fonts.googleapis.com/css2?family=Arimo:wght@400;700&display=swap">
<style>
  :root {
    --page-bg: #ffffff;
    --brand-blue: #1a3fe0;
    --brand-navy: #0a0f86;
    --ink: #111111;
    --on-band: #ffffff;
  }
  html, body {
    margin: 0;
    padding: 0;
    width: 1200px;
    height: 1000px;
    overflow: hidden;
    background: var(--page-bg);
  }
  .canvas {
    position: relative;
    width: 1200px;
    height: 1000px;
    font-family: "Arimo", Arial, sans-serif;
  }
  .business-card {
    position: absolute;
    left: 181px;
    top: 270px;
    width: 852px;
    height: 493px;
    background: var(--page-bg);
  }
  .brand-name {
    position: absolute;
    left: 0;
    right: 0;
    top: 95px;
    margin: 0;
    text-align: center;
    font-size: 66px;
    font-weight: 400;
    letter-spacing: 1px;
    line-height: 1;
    color: var(--brand-blue);
    text-transform: uppercase;
  }
  .contact-details {
    position: absolute;
    left: 0;
    right: 0;
    top: 184px;
    margin: 0;
    text-align: center;
    font-style: normal;
    font-size: 29px;
    line-height: 40.5px;
    color: var(--ink);
    letter-spacing: 0.3px;
  }
  .contact-details span { display: block; }
  .web-band {
    position: absolute;
    left: 0;
    bottom: 0;
    width: 100%;
    height: 50px;
    background: linear-gradient(90deg, var(--brand-navy) 0%, var(--brand-blue) 100%);
    color: var(--on-band);
    font-size: 34px;
    line-height: 50px;
    text-align: center;
    letter-spacing: 0.5px;
  }
</style>
</head>
<body>
  <main class="canvas">
    <section class="business-card">
      <h1 class="brand-name">Larkfield Checks</h1>
      <address class="contact-details">
        <span class="associate-name">Associate name</span>
        <span class="address-line">Address</span>
        <span class="address-line">Address</span>
        <span class="address-line">Address</span>
        <span class="phone">08450 555 210</span>
        <span class="email">mail@larkfieldchecks.co.uk</span>
      </address>
      <div class="web-band">www.larkfieldchecks.co.uk</div>
    </section>
  </main>
</body>
</html>
```